BRIXLEY ELECTRICAL

all black background with silver and lime writing, fonts i like are gothic style but am open to ideas, will need a picture logo aswell as im putting this on my van.i am a electrical contractor starting up my own electrical business. underneath brixley electrical heading on card we could put" professiona cost effective soloutions to all your electrical needs".{ or something of that nature }.on aback of card on top half list servises provided, real estate and commercial maintenance, new home and renovation rewires and upgrades, split system air conditioning, floor heat, tv phone data, smoke detoctors, lighting systems , builders welcome, , and also a thankyou for your business.

Industry/Entity Type

Real Estate

Contact Information for Business Card

GAVIN PRESTWORTH
brixleyelectrical@quillnet.com.au
0417352940
lic no 81926
ac lic no l593721
abn 37216405813

```html
<!DOCTYPE html>
<html lang="en">
<head>
<meta charset="utf-8">
<title>Brixley Electrical – Business Card</title>
<link rel="stylesheet" href="https://fonts.googleapis.com/css2?family=Open+Sans:wght@400;600&display=swap">
<style>
  :root {
    --stage: #6b5a44;
    --card: #0b0b0b;
    --card-edge: #1c1c1c;
    --lime: #8ee21c;
    --silver: #e4e4e4;
    --silver-dim: #bdbdbd;
  }
  * { margin: 0; padding: 0; box-sizing: border-box; }
  html, body { width: 1200px; height: 1023px; overflow: hidden; }
  body {
    background: var(--stage);
    font-family: "Open Sans", Arial, sans-serif;
    position: relative;
  }
  .card {
    position: absolute;
    background: linear-gradient(160deg, #1a1a1a 0%, var(--card) 45%, #050505 100%);
    border: 1px solid var(--card-edge);
    box-shadow: 0 14px 30px rgba(0,0,0,.45);
    color: var(--silver);
  }

  /* Back of card */
  .card-back { left: 150px; top: 100px; width: 600px; height: 340px; }
  .services-title {
    position: absolute; left: 0; right: 0; top: 38px;
    text-align: center; color: var(--lime); font-weight: 600; font-size: 17px;
  }
  .services-rule {
    position: absolute; left: 120px; right: 120px; top: 68px;
    height: 1px; background: var(--lime);
  }
  .services-list {
    position: absolute; left: 90px; width: 330px; top: 80px;
    list-style: none; text-align: center; font-size: 16px; line-height: 25px;
  }
  .back-brand {
    position: absolute; right: 36px; top: 180px;
    display: flex; align-items: center; gap: 10px;
    color: var(--lime); font-weight: 600; font-size: 17px; letter-spacing: .5px;
  }
  .brand-dot { width: 28px; height: 28px; border-radius: 50%; background: var(--lime); }
  .back-footer {
    position: absolute; left: 0; right: 0; bottom: 22px;
    text-align: center; font-size: 13px; color: var(--silver-dim);
  }

  /* Front of card */
  .card-front { left: 240px; top: 470px; width: 740px; height: 420px; }
  .front-brand {
    position: absolute; left: 0; top: 115px;
    display: flex; align-items: center; gap: 16px; padding-left: 40px;
    color: var(--lime); font-weight: 600; font-size: 50px; letter-spacing: 1px;
  }
  .front-brand .brand-dot { width: 70px; height: 70px; }
  .tagline-band {
    position: absolute; left: 196px; right: 46px; top: 190px; height: 24px;
    background: var(--lime); color: #0b0b0b;
    font-size: 15px; font-weight: 600; line-height: 24px; text-align: center;
  }
  .contact {
    position: absolute; top: 285px; right: 380px; text-align: right;
    font-size: 17px; line-height: 26px;
  }
  .contact-name { color: var(--lime); font-weight: 600; font-size: 20px; letter-spacing: .5px; }
  .contact-row { display: flex; align-items: center; justify-content: flex-end; gap: 10px; }
  .contact-row svg { width: 16px; height: 16px; }
  .divider {
    position: absolute; left: 388px; top: 290px; width: 1px; height: 72px; background: var(--lime);
  }
  .credentials {
    position: absolute; left: 414px; top: 288px; font-size: 17px; line-height: 25px;
  }
</style>
</head>
<body>

<section class="card card-back" aria-label="Back of business card">
  <h2 class="services-title">Services Provided:</h2>
  <div class="services-rule"></div>
  <ul class="services-list">
    <li>Real estate and commercial maintenance</li>
    <li>New home and renovation rewires and upgrades</li>
    <li>Split system air conditioning</li>
    <li>Floor heat</li>
    <li>TV phone data</li>
    <li>Smoke detectors</li>
    <li>Lighting systems</li>
  </ul>
  <div class="back-brand"><span class="brand-dot"></span>BRIXLEY ELECTRICAL</div>
  <p class="back-footer">Builders welcome &nbsp;and also a thankyou for your business</p>
</section>

<section class="card card-front" aria-label="Front of business card">
  <div class="front-brand"><span class="brand-dot"></span>BRIXLEY ELECTRICAL</div>
  <div class="tagline-band">Professional cost effective soloutions to all your electrical needs</div>

  <div class="contact">
    <div class="contact-name">GAVIN PRESTWORTH</div>
    <div class="contact-row">041 735 2940
      <svg viewBox="0 0 16 16" aria-hidden="true"><rect x="4" y="1" width="8" height="14" rx="1.5" fill="none" stroke="#8ee21c" stroke-width="1.5"/><circle cx="8" cy="12.5" r="1" fill="#8ee21c"/></svg>
    </div>
    <div class="contact-row">brixleyelectrical@quillnet.com.au
      <svg viewBox="0 0 16 16" aria-hidden="true"><rect x="1" y="3" width="14" height="10" fill="#8ee21c"/><path d="M1 3l7 6 7-6" fill="none" stroke="#0b0b0b" stroke-width="1.3"/></svg>
    </div>
  </div>
  <div class="divider"></div>
  <div class="credentials">
    <div>License No : 81926</div>
    <div>AC Licence No : 593721</div>
    <div>ABN : 37216405813</div>
  </div>
</section>

</body>
</html>
```